DESIGN specific documents

We need precise design of certain documents and certain, for our law firm. Specifically we seek: 1) Design a format for report or legal report (legal opinion) 2) Design of a format fee proposal (proposal fee) 3) Design template PPT 4) Website design Designs must take our corporate logo and a simulated document structure proposals must come the word format in addition to the classic vector file formats

Target Market(s)

Business

Industry/Entity Type

Legal

Number of Pages Required

3 page

Requirements
Must have
• Corporate Logo Design Report attached should consider a cover and report sheets
Nice to have
• simulate a design on recycled paper

```html
<!DOCTYPE html>
<html lang="en">
<head>
<meta charset="utf-8">
<title>Valmora y Cía Abogados – Document Suite</title>
<link href="https://fonts.googleapis.com/css2?family=Crimson+Text:ital,wght@0,400;1,400;1,700&family=Open+Sans:ital,wght@0,300;0,400;0,700;1,300&display=swap" rel="stylesheet">
<style>
  :root{
    --blue:#0f5a7e;
    --blue-dark:#0b4a69;
    --grey:#8f9295;
    --grey-light:#f1f2f3;
    --grey-row:#ecedee;
    --ink:#4a4f55;
    --stage:#2c2c2d;
    --white:#ffffff;
  }
  *{box-sizing:border-box;margin:0;padding:0}
  html,body{width:1200px;height:1200px;overflow:hidden;background:var(--stage)}
  .canvas{position:relative;width:1200px;height:1200px}
  .doc{position:absolute;overflow:hidden}

  /* ---------- Fee proposal sheet ---------- */
  .fee{left:52px;top:36px;width:524px;height:678px;background:var(--white);
       font-family:"Crimson Text",serif;color:var(--ink)}
  .fee .abs{position:absolute}
  .firm-name{font-family:"Crimson Text",serif;color:#3d6f8c;font-weight:400;letter-spacing:.5px;line-height:1.15;text-align:center}
  .fee .firm-name{left:16px;top:52px;width:132px;font-size:17px}
  .fee .firm-name small{display:block;font-size:8px;letter-spacing:4px}
  .fee .brand-square{left:70px;top:18px;width:26px;height:26px;background:#3d6f8c}
  .fee-title{left:356px;top:22px;width:168px;height:32px;background:var(--blue);color:var(--white);
             font-style:italic;font-size:24px;line-height:32px;padding-left:18px}
  .fee-date{left:370px;top:68px;font-style:italic;font-size:12px;line-height:18px}
  .band{left:0;width:524px;background:var(--grey-light)}
  .section-label{left:0;width:102px;background:var(--blue);color:var(--white);font-style:italic;font-weight:700;
                 font-size:12px;line-height:14px;padding:5px 8px;text-transform:uppercase;display:flex;align-items:center}
  .field{left:114px;width:398px;font-style:italic;font-size:8px;display:flex;gap:6px;white-space:nowrap}
  .field span{flex:1;border-bottom:1px dotted #7b8086;height:9px}
  .field b{font-weight:400}
  .consult-text{left:113px;top:424px;width:392px;font-style:italic;font-size:8.3px;line-height:13.5px}
  .schedule-text{left:10px;top:560px;width:158px;font-style:italic;font-size:5.6px;line-height:13.5px}
  .schedule{left:195px;top:518px;width:318px;border-collapse:separate;border-spacing:3px 3px;
            font-style:italic;font-size:8.5px;text-align:center}
  .schedule td{background:var(--grey-row);height:16px;width:50%}
  .signature{left:20px;top:640px;width:490px;font-style:italic;font-size:11px;display:flex;justify-content:space-between}
  .foot-grey{left:0;top:664px;width:253px;height:14px;background:#6f7a82}
  .foot-blue{left:253px;top:664px;width:271px;height:14px;background:var(--blue)}

  /* ---------- Annual report cover ---------- */
  .cover{left:604px;top:36px;width:528px;height:682px;background:var(--blue);font-family:"Open Sans",sans-serif;color:var(--white)}
  .cover .abs{position:absolute}
  .cover-photo-left{left:0;top:0;width:44px;height:310px;background:linear-gradient(160deg,#b9c6d2,#6f8aa3 60%,#9fb2c3)}
  .cover-column{left:44px;top:0;width:158px;height:682px;background:var(--grey)}
  .cover-photo-right{left:202px;top:0;width:326px;height:310px;background:linear-gradient(170deg,#dfe9f3 0%,#8fb2cf 35%,#4f7898 70%,#6f8f6a 100%)}
  .cover .firm-name{left:44px;top:78px;width:158px;color:var(--white);font-family:"Crimson Text",serif;font-size:15px}
  .cover .firm-name small{display:block;font-size:7px;letter-spacing:4px}
  .cover .brand-square{left:111px;top:44px;width:24px;height:24px;background:var(--white)}
  .cover-circle{left:12px;top:214px;width:228px;height:228px;border-radius:50%;border:3px solid var(--white);
                background:radial-gradient(circle at 35% 65%,#e7d9cc 0%,#cdb9a8 30%,#5b5d60 60%,#2f3236 100%)}
  .cover-title{left:242px;top:414px;font-style:italic;font-weight:300;font-size:21px;line-height:32px;letter-spacing:.3px}
  .cover-contact{left:202px;top:620px;width:326px;text-align:center;font-size:8.6px;line-height:14px}
  .cover-contact strong{display:block;font-size:11.5px;margin-bottom:6px}

  /* ---------- Presentation welcome slide ---------- */
  .slide{left:305px;top:754px;width:558px;height:418px;background:var(--blue);font-family:"Open Sans",sans-serif;color:var(--white)}
  .slide .abs{position:absolute}
  .slide-photo{left:0;top:18px;width:558px;height:234px;background:linear-gradient(160deg,#e6e8ea 0%,#b3b8bd 40%,#8e959b 75%,#c6cacd 100%)}
  .slide-topband{left:0;top:0;width:558px;height:18px;background:var(--blue)}
  .slide .firm-name{left:40px;top:150px;width:184px;font-size:26px;color:#3d6f8c}
  .slide .firm-name small{display:block;font-size:11px;letter-spacing:7px}
  .slide .brand-square{left:107px;top:76px;width:48px;height:48px;background:#3d6f8c}
  .slide-bottom{left:0;top:252px;width:558px;height:166px;background:linear-gradient(180deg,#0f5a7e,#0c4e70)}
  .slide-bar{left:164px;top:242px;width:224px;height:14px;background:var(--blue-dark)}
  .slide-welcome{right:31px;top:276px;text-align:right}
  .slide-welcome h1{font-weight:700;font-size:36px;line-height:42px;letter-spacing:.5px}
  .slide-welcome p{font-size:18px;line-height:24px;margin-top:2px}
  .slide-contact{left:18px;top:374px;display:flex;gap:10px;font-size:8.6px;line-height:13px}
  .slide-contact div{display:flex;flex-direction:column}
  .slide-contact svg{vertical-align:-1px;margin-right:3px}
</style>
</head>
<body>
<div class="canvas">

  <!-- Fee proposal form -->
  <section class="doc fee" aria-label="Fee proposal form">
    <div class="abs brand-square"></div>
    <div class="abs firm-name">VALMORA Y CÍA<small>ABOGADOS</small></div>

    <div class="abs fee-title">Fee Proposal</div>
    <div class="abs fee-date">Date: (DD/MM/YYYY)<br>.........../............ /..............</div>

    <div class="abs section-label" style="top:154px;height:38px">Client<br>Information</div>
    <div class="abs field" style="top:135px"><b>Last Name :</b><span></span><b>First Name :</b><span></span></div>
    <div class="abs field" style="top:157px"><b>Company Name :</b><span></span></div>
    <div class="abs field" style="top:179px"><b>Contact No :</b><span></span><b>Email :</b><span></span></div>
    <div class="abs field" style="top:201px"><b>Website Address :</b><span></span></div>

    <div class="abs band" style="top:222px;height:82px"></div>
    <div class="abs section-label" style="top:242px;height:39px">Proposal<br>Information</div>
    <div class="abs field" style="top:230px"><b>Project Name :</b><span></span></div>
    <div class="abs field" style="top:256px"><b>Reference Number:</b><span></span><b>Revision Number :</b><span></span></div>
    <div class="abs field" style="top:281px"><b>Data Submitted :</b><span></span></div>

    <div class="abs section-label" style="top:350px;height:38px">Project<br>Details</div>
    <div class="abs field" style="top:328px"><b>Lorem Ipsum :</b><span></span></div>
    <div class="abs field" style="top:347px"><b>Lorem Ipsum :</b><span></span></div>
    <div class="abs field" style="top:366px"><b>Lorem Ipsum :</b><span></span></div>
    <div class="abs field" style="top:384px"><b>Lorem Ipsum :</b><span></span></div>

    <div class="abs band" style="top:410px;height:82px"></div>
    <div class="abs section-label" style="top:434px;height:38px;font-size:10px">Consultatants</div>
    <p class="abs consult-text">Lorem ipsum dolor sit amet, consectetur adipiscing elit. Sed at ante. Mauris eleifend, quam a vulptate dictum, massa quam dapibus leo, eget vulputate orci purus ut lorem. In fringilla mi in ligula. Pellen tesque aliquam quam vel dolor. Nunc adipiscing. Sed quamodio, tempus ac, aliquam molestie varius ac, tellus. Vestibulum ut nulla aliquam risus rutrum interdum. Pellentesque lorem.</p>

    <div class="abs section-label" style="top:513px;height:38px">Project<br>Schedule</div>
    <p class="abs schedule-text">Lorem ipsum dolor sit amet, consectetur adipiscing elit. Sed at ante. Mauris eleifend, quam a vulptate dictum, massa quam dapibus leo, eget vulputate orci purus ut lorem. In</p>
    <table class="abs schedule">
      <tr><td>Work Stage</td><td>Duration</td></tr>
      <tr><td>Lorem Ipsum</td><td>Lorem Ipsum</td></tr>
      <tr><td>Lorem Ipsum</td><td>Lorem Ipsum</td></tr>
      <tr><td>Lorem Ipsum</td><td>Lorem Ipsum</td></tr>
      <tr><td>Lorem Ipsum</td><td>Lorem Ipsum</td></tr>
    </table>

    <div class="abs signature"><span>Signature: .......................................</span><span>Archiect / Client initials ............. /.............</span></div>
    <div class="abs foot-grey"></div>
    <div class="abs foot-blue"></div>
  </section>

  <!-- Annual legal report cover -->
  <section class="doc cover" aria-label="Annual legal report cover">
    <div class="abs cover-photo-left" role="img" aria-label="Photo of glass office tower facade"></div>
    <div class="abs cover-column"></div>
    <div class="abs cover-photo-right" role="img" aria-label="Photo of glass office tower against a blue sky"></div>
    <div class="abs brand-square"></div>
    <div class="abs firm-name">VALMORA Y CÍA<small>ABOGADOS</small></div>
    <div class="abs cover-circle" role="img" aria-label="Photo of a hand signing a document with a pen"></div>
    <h2 class="abs cover-title">2016 - 2017 ANNUAL<br>COMPANY LEGAL REPORT</h2>
    <div class="abs cover-contact">
      <strong>VALMORA Y CÍA. ABOGADOS</strong>
      56 2 2555 0148 • 56 2 2555 0149 | info@valmora.cl | www.valmora.cl<br>
      Av. Alameda Norte 1420, Of. 310, Providencia, Santiago, PO BOX : CP 7500000
    </div>
  </section>

  <!-- Presentation title slide -->
  <section class="doc slide" aria-label="Presentation title slide">
    <div class="abs slide-photo" role="img" aria-label="Photo looking up at a glass office building under a cloudy sky"></div>
    <div class="abs slide-topband"></div>
    <svg class="abs" style="left:0;top:0" width="558" height="60" aria-hidden="true">
      <polygon points="119,18 147,18 133,46" fill="#0f5a7e"/>
    </svg>
    <div class="abs brand-square"></div>
    <div class="abs firm-name">VALMORA Y CÍA<small>ABOGADOS</small></div>
    <div class="abs slide-bottom"></div>
    <div class="abs slide-bar"></div>
    <svg class="abs" style="left:0;top:250px" width="558" height="60" aria-hidden="true">
      <polyline points="0,53 74,53 74,13 139,13" fill="none" stroke="#2a8cc0" stroke-width="1"/>
      <line x1="151" y1="13" x2="558" y2="13" stroke="#2a8cc0" stroke-width="1"/>
      <line x1="163" y1="17" x2="558" y2="17" stroke="#2a8cc0" stroke-width="1"/>
      <circle cx="145" cy="13" r="5.5" fill="#2aa0d8" stroke="#ffffff" stroke-width="1"/>
    </svg>
    <div class="abs slide-welcome">
      <h1>WELCOME</h1>
      <p>TO OUR PRESENTATION</p>
    </div>
    <div class="abs slide-contact">
      <div>
        <span><svg width="9" height="8" viewBox="0 0 9 8"><path d="M0 2 Q4.5 -1 9 2 L7.5 3.5 L6 2.5 L3 2.5 L1.5 3.5 Z M2 4 H7 L8 8 H1 Z" fill="#fff"/></svg>56 2 2555 0148</span>
        <span><svg width="9" height="8" viewBox="0 0 9 8"><path d="M0 2 Q4.5 -1 9 2 L7.5 3.5 L6 2.5 L3 2.5 L1.5 3.5 Z M2 4 H7 L8 8 H1 Z" fill="#fff"/></svg>56 2 2555 0149</span>
      </div>
      <div>
        <span><svg width="9" height="9" viewBox="0 0 10 10"><circle cx="5" cy="5" r="4.3" fill="none" stroke="#fff"/><path d="M0.7 5 H9.3 M5 0.7 V9.3 M5 0.7 Q1.5 5 5 9.3 M5 0.7 Q8.5 5 5 9.3" fill="none" stroke="#fff" stroke-width=".8"/></svg>www.valmora.cl</span>
        <span><svg width="9" height="7" viewBox="0 0 9 7"><rect width="9" height="7" fill="#fff"/><path d="M0 0 L4.5 3.5 L9 0" fill="none" stroke="#0f5a7e" stroke-width=".8"/></svg>info@valmora.cl</span>
      </div>
      <div>
        <span><svg width="9" height="8" viewBox="0 0 9 8"><path d="M4.5 0 L9 4 H7.5 V8 H5.5 V5.5 H3.5 V8 H1.5 V4 H0 Z" fill="#fff"/></svg>Av. Alameda Norte 1420, Of. 310</span>
        <span style="padding-left:12px">Providencia, Santiago, PO BOX : CP 7500000</span>
      </div>
    </div>
  </section>

</div>
</body>
</html>
```